Business Card - Professional Minimalist - Double sided

We appreciate minimalist logo/web/collateral designs that allow design to tell a story. We want to relay a professional image/approach but throwing in a splash of modern when we’re able so long as it’s not distracting. Think 75% classic corporate, 25% modern. Open to black or white design, not sure which might look the best.

Target Market(s)

Senior executives or related government affairs contacts within the agriculture, energy, and defense industries (i.e., potential clients) but located outside of Washington, DC. Most potential clients based in DC with be familiar with both of us and our shared history.

Industry/Entity Type

Consulting

Contact Information for Business Card

Name: Daniel R. Whitlock
Title: Co-Founder & Partner
Address: 418 Bramblewood Ave. SE | Suite 2716 | Washington, D.C. 20019
Phone: (202) 555-0187
Email: Daniel@HollerbyWhitlock.com

Font styles to use
Serif

Colors

Designer to choose only greyscale colors for use in the design.

Requirements
Must have
• Name: Daniel R. Whitlock
Phone: (202) 555-0187

```html
<!DOCTYPE html>
<html lang="en">
<head>
<meta charset="utf-8">
<title>Hollerby Whitlock Group – Business Card</title>
<link rel="stylesheet" href="https://fonts.googleapis.com/css2?family=Open+Sans:wght@400;600&family=Raleway:wght@700&family=Marcellus&display=swap">
<style>
  :root {
    --stage: #b7b7b7;
    --card-dark: #58585a;
    --card-light: #ffffff;
    --text-light: #ffffff;
    --text-soft: #e4e4e6;
    --text-dark: #4d4d4f;
    --accent-grey: #a7a8ab;
  }
  html, body {
    margin: 0;
    padding: 0;
    width: 1200px;
    height: 801px;
    overflow: hidden;
    background: var(--stage);
  }
  .stage {
    position: relative;
    width: 1200px;
    height: 801px;
  }
  .card {
    position: absolute;
    top: 274px;
    width: 443px;
    height: 263px;
    overflow: hidden;
  }
  .card--front {
    left: 153px;
    background: var(--card-dark);
  }
  .card--back {
    left: 625px;
    background: var(--card-light);
  }
  .emblem-area {
    position: absolute;
    left: 265px;
    top: 19px;
    width: 178px;
    height: 226px;
    border-radius: 0 0 0 62px;
    background: linear-gradient(135deg, var(--card-light) 0%, var(--accent-grey) 55%, var(--card-light) 100%);
  }
  .contact {
    position: absolute;
    left: 25px;
    top: 62px;
    color: var(--text-soft);
    font-family: "Open Sans", Arial, sans-serif;
  }
  .contact__name {
    margin: 0;
    font-family: "Raleway", "Open Sans", sans-serif;
    font-weight: 700;
    font-size: 17px;
    line-height: 20px;
    color: var(--text-light);
    text-transform: uppercase;
  }
  .contact__title {
    margin: 0 0 5px;
    font-size: 11.5px;
    line-height: 15px;
    text-transform: uppercase;
  }
  .contact__list {
    list-style: none;
    margin: 0 0 4px;
    padding: 0;
  }
  .contact__item {
    display: flex;
    align-items: center;
    gap: 5px;
    font-size: 12px;
    line-height: 16.5px;
  }
  .contact__icon {
    width: 12px;
    height: 12px;
    flex: none;
  }
  .contact__address {
    margin: 0;
    font-style: normal;
    font-size: 11.5px;
    line-height: 16px;
  }
  .brand {
    position: absolute;
    left: 0;
    right: 0;
    top: 115px;
    display: flex;
    justify-content: center;
    align-items: center;
    gap: 12px;
  }
  .brand__mark {
    width: 30px;
    height: 30px;
    background: var(--text-dark);
  }
  .brand__name {
    font-family: "Marcellus", Georgia, serif;
    font-weight: 400;
    font-size: 21px;
    letter-spacing: 0.5px;
    color: var(--text-dark);
    text-transform: uppercase;
  }
</style>
</head>
<body>
<main class="stage">
  <section class="card card--front" aria-label="Card front">
    <div class="emblem-area" role="img" aria-label="Large brand emblem decoration"></div>
    <div class="contact">
      <h1 class="contact__name">Daniel R. Whitlock</h1>
      <p class="contact__title">Co-Founder &amp; Partner</p>
      <ul class="contact__list">
        <li class="contact__item">
          <svg class="contact__icon" viewBox="0 0 24 24" aria-hidden="true"><path fill="#fff" d="M6.6 10.8a15 15 0 0 0 6.6 6.6l2.2-2.2c.3-.3.7-.4 1-.2 1.1.4 2.3.6 3.6.6.6 0 1 .4 1 1V20c0 .6-.4 1-1 1A17 17 0 0 1 3 4c0-.6.4-1 1-1h3.5c.6 0 1 .4 1 1 0 1.3.2 2.5.6 3.6.1.3 0 .7-.2 1z"/></svg>
          (202) 555-0187
        </li>
        <li class="contact__item">
          <svg class="contact__icon" viewBox="0 0 24 24" aria-hidden="true"><rect x="2" y="5" width="20" height="14" fill="#fff"/><path d="M2 5l10 8 10-8" fill="none" stroke="#58585a" stroke-width="1.6"/></svg>
          Daniel@HollerbyWhitlock.com
        </li>
        <li class="contact__item">
          <svg class="contact__icon" viewBox="0 0 24 24" aria-hidden="true"><g fill="none" stroke="#fff" stroke-width="1.8"><circle cx="12" cy="12" r="10"/><ellipse cx="12" cy="12" rx="4.5" ry="10"/><path d="M2 12h20M4 7h16M4 17h16"/></g></svg>
          www.HollerbyWhitlock.com
        </li>
      </ul>
      <address class="contact__address">418 Bramblewood Ave. SE | Suite<br>2716 | Washington, D.C. 20019</address>
    </div>
  </section>

  <section class="card card--back" aria-label="Card back">
    <div class="brand">
      <span class="brand__mark" aria-hidden="true"></span>
      <span class="brand__name">Hollerby Whitlock Group</span>
    </div>
  </section>
</main>
</body>
</html>
```